Tallgrove Vale Management

I need a professional website. My current website is tallgrovevalemanagement.com and I hate it. It was created with some AI tool very quickly because I needed a site up and running with no advanced notice. I’m open to all designs .. I trust you, the professionals will deliver the results I’m anxiously awaiting! :)

```html
<!DOCTYPE html>
<html lang="en">
<head>
<meta charset="utf-8">
<title>Tallgrove Vale Management</title>
<link rel="stylesheet" href="https://fonts.googleapis.com/css2?family=Cormorant+Garamond:wght@400;500&family=Inter:wght@400;500;600&display=swap">
<style>
:root{
  --navy:#3d4d73;
  --navy-deep:#1f2d54;
  --navy-cta:#2f4066;
  --cream:#faf8f3;
  --white:#ffffff;
  --ink:#2b2f38;
  --muted:#7d828c;
  --line:#ebe8e1;
  --green:#5d7f5b;
  --green-soft:#e8efe6;
  --serif:'Cormorant Garamond', Georgia, serif;
  --sans:'Inter', Arial, sans-serif;
}
*{box-sizing:border-box;margin:0;padding:0}
html,body{width:1200px;height:4222px;overflow:hidden}
body{font-family:var(--sans);color:var(--ink);background:var(--white);position:relative}
.wrap{width:770px;margin:0 auto;position:relative}
.label{font-size:8px;letter-spacing:2px;text-transform:uppercase;color:var(--green);font-weight:500}
.h2{font-family:var(--serif);font-weight:400;color:var(--ink);font-size:30px;line-height:1.05}
.center{text-align:center}
.btn{display:inline-flex;align-items:center;gap:6px;background:var(--navy);color:#fff;font-size:10px;font-weight:600;border-radius:20px;padding:0 20px;height:33px}
.btn svg{width:9px;height:9px}
.photo{border-radius:8px}
.photo-green{background:linear-gradient(180deg,#b9c7d3 0%,#8ea08a 28%,#4f6e3e 60%,#3d5a33 100%)}
.photo-wood{background:radial-gradient(ellipse at 50% 60%,#d9b68c 0%,#b89c7c 25%,#d6d2ca 55%,#bfb8ac 100%)}
.photo-room{background:linear-gradient(120deg,#4a3a2b 0%,#a78a68 45%,#d7c4a8 75%,#3a2d22 100%)}

/* nav */
.nav{height:62px;background:#f4f4f4;border-bottom:1px solid #e2e2e2}
.nav .wrap{display:flex;align-items:center;height:62px}
.brand{display:flex;align-items:center;gap:8px;font-family:var(--serif);font-size:14px;color:var(--navy-deep);font-weight:500}
.brand .mark{width:28px;height:28px;border-radius:50%;background:var(--navy-deep)}
.nav-links{margin-left:auto;display:flex;gap:20px;font-size:9.5px;color:var(--ink)}
.nav .btn{margin-left:26px;height:26px;padding:0 14px;font-size:9px}

/* hero */
.hero{height:343px;background:linear-gradient(180deg,rgba(32,44,78,.72),rgba(32,44,78,.78)),linear-gradient(160deg,#8c9fc0 0%,#4b5f86 40%,#7f92b4 70%,#3c4f77 100%);text-align:center;color:#fff;padding-top:70px}
.hero h1{font-family:var(--serif);font-weight:400;font-size:41px;line-height:1.1;width:460px;margin:0 auto}
.hero p{font-size:12.5px;line-height:1.45;width:420px;margin:18px auto 0;color:#e4e8f1}
.hero-actions{display:flex;justify-content:center;gap:14px;margin-top:22px}
.btn-ghost{background:transparent;border:1px solid rgba(255,255,255,.7)}
.hero .btn{height:36px}

/* features */
.features{height:131px;border-bottom:1px solid var(--line)}
.features .wrap{display:grid;grid-template-columns:repeat(4,1fr);gap:20px;padding-top:42px;text-align:center}
.feature h3{font-family:var(--serif);font-weight:400;font-size:12px;color:var(--ink)}
.feature p{font-size:8.5px;line-height:1.6;color:var(--muted);margin-top:6px}

/* about */
.about{height:464px;position:relative}
.about-pic{position:absolute;background:#fff;border-radius:8px;box-shadow:0 6px 18px rgba(0,0,0,.12);padding-bottom:20px}
.about-pic .photo{width:100%;height:100%}
.about-text{position:absolute;left:620px;top:82px;width:365px}
.about-text .h2{margin-top:12px;font-size:29px}
.about-text p{font-size:10.5px;line-height:1.75;color:var(--muted);margin-top:18px}
.checks{list-style:none;margin-top:16px}
.checks li{display:flex;align-items:center;gap:9px;font-size:9.5px;font-weight:500;margin-bottom:9px}
.tick{width:12px;height:12px;border-radius:50%;background:var(--green-soft);display:flex;align-items:center;justify-content:center}
.tick svg{width:7px;height:7px}
.about-text .btn{margin-top:12px}

/* services */
.services{height:582px;background:var(--cream);padding-top:83px}
.services .h2{margin-top:8px}
.svc-grid{display:grid;grid-template-columns:repeat(4,1fr);gap:15px;margin-top:38px}
.svc{background:#fff;border-radius:8px;overflow:hidden;box-shadow:0 1px 3px rgba(0,0,0,.05)}
.svc-body{height:95px;padding:16px 15px}
.svc h3{font-family:var(--serif);font-weight:400;font-size:12px}
.svc p{font-size:8.5px;line-height:1.65;color:var(--muted);margin-top:5px}
.svc .photo{height:140px;border-radius:0}
.services .cta-row{text-align:center;margin-top:30px}

/* why */
.why{height:505px;position:relative}
.why-text{position:absolute;left:215px;top:93px;width:370px}
.why-text .h2{margin-top:10px;font-size:29px}
.why-item{display:flex;gap:14px;margin-top:20px}
.why-item:first-of-type{margin-top:28px}
.why-icon{width:34px;height:34px;border-radius:8px;background:var(--green-soft);flex:none;display:flex;align-items:center;justify-content:center}
.why-icon svg{width:14px;height:14px}
.why-item h3{font-family:var(--serif);font-weight:400;font-size:12px}
.why-item p{font-size:9px;line-height:1.7;color:var(--muted);margin-top:5px}
.why-pic{position:absolute;left:620px;top:78px;width:365px;height:350px;border-radius:10px;box-shadow:0 10px 28px rgba(0,0,0,.15)}

/* projects */
.projects{height:557px;background:var(--cream);padding-top:82px}
.projects .h2{margin-top:6px}
.proj-grid{display:grid;grid-template-columns:1fr 1fr;gap:20px;margin-top:36px}
.proj{height:238px;position:relative;border-radius:8px;box-shadow:0 6px 16px rgba(0,0,0,.12)}
.proj span{position:absolute;left:20px;bottom:22px;font-family:var(--serif);font-size:15px;color:#fff}
.projects .cta-row{text-align:center;margin-top:30px}

/* testimonials */
.testimonials{height:392px;padding-top:83px}
.testimonials .h2{margin-top:6px}
.tst-grid{display:grid;grid-template-columns:1fr 1fr;gap:20px;margin-top:38px}
.tst{background:var(--cream);border-radius:8px;height:145px;padding:20px 21px}
.stars{display:flex;gap:2px}
.stars svg{width:10px;height:10px}
.tst blockquote{font-family:var(--serif);font-style:italic;font-size:10px;line-height:1.85;color:var(--muted);margin-top:12px}
.tst h4{font-family:var(--serif);font-weight:400;font-size:11px;margin-top:16px}
.tst small{font-size:8px;color:var(--muted)}

/* cta */
.cta{height:275px;background:var(--navy-cta);text-align:center;color:#fff;padding-top:72px}
.cta h2{font-family:var(--serif);font-weight:400;font-size:29px}
.cta p{font-size:11px;line-height:1.7;color:#d1d7e4;width:380px;margin:14px auto 0}
.cta .btn{background:#fff;color:var(--navy);margin-top:18px;height:34px}

/* contact */
.contact{height:631px;background:var(--cream);padding-top:84px}
.contact .h2{margin-top:6px;width:440px;margin-left:auto;margin-right:auto}
.contact .sub{font-size:11px;color:var(--muted);margin-top:10px}
.contact-grid{position:relative;margin-top:38px;height:380px}
.info-card{position:absolute;left:0;top:0;width:290px;height:163px;background:#fff;border-radius:8px;padding:22px 20px}
.info-card h3{font-family:var(--serif);font-weight:400;font-size:14px}
.info-row{display:flex;align-items:center;gap:12px;margin-top:14px}
.info-ic{width:24px;height:24px;border-radius:6px;background:var(--green-soft);display:flex;align-items:center;justify-content:center;flex:none}
.info-ic svg{width:11px;height:11px}
.info-row small{display:block;font-size:6.5px;letter-spacing:1.5px;color:var(--muted);text-transform:uppercase}
.info-row span{font-size:9.5px}
.form-card{position:absolute;left:320px;top:0;width:450px;height:378px;background:#fff;border-radius:8px;padding:24px 24px}
.form-card label{display:block;font-size:6.5px;letter-spacing:1.5px;text-transform:uppercase;color:var(--ink);margin-bottom:6px}
.field{background:var(--cream);border:1px solid var(--line);border-radius:5px;height:30px;font-size:9px;color:#b3b5ba;padding:9px 11px}
.row2{display:grid;grid-template-columns:1fr 1fr;gap:14px}
.fgroup{margin-bottom:14px}
.field.tall{height:92px}
.field.dark{color:var(--ink)}
.submit{width:100%;height:34px;border-radius:5px;background:var(--navy);color:#fff;font-size:10px;font-weight:600;display:flex;align-items:center;justify-content:center;gap:7px;margin-top:10px}
.submit svg{width:10px;height:10px}

/* footer */
.footer{height:280px;background:var(--navy-deep);color:#c3cadb;padding-top:52px;position:relative}
.foot-grid{display:grid;grid-template-columns:repeat(4,200px);font-size:8.5px}
.foot-grid .brand{color:#fff}
.foot-grid .brand .mark{background:#fff}
.foot-about{line-height:1.7;margin-top:14px;width:160px}
.socials{display:flex;gap:8px;margin-top:14px}
.socials i{width:20px;height:20px;border-radius:50%;border:1px solid rgba(255,255,255,.3);display:block}
.foot-col h4{font-size:7.5px;letter-spacing:2px;color:#fff;font-weight:500;margin-bottom:12px}
.foot-col p{margin-bottom:11px;display:flex;align-items:center;gap:7px}
.foot-col svg{width:9px;height:9px}
.copy{position:absolute;left:215px;right:215px;bottom:24px;border-top:1px solid rgba(255,255,255,.1);padding-top:12px;display:flex;justify-content:space-between;font-size:7.5px;color:#8b94ab}
</style>
</head>
<body>

<header class="nav">
  <div class="wrap">
    <div class="brand"><span class="mark"></span>Tallgrove Vale</div>
    <nav class="nav-links"><span>Home</span><span>About</span><span>Services</span><span>Why Us</span><span>Projects</span><span>Contact</span></nav>
    <span class="btn"><svg viewBox="0 0 24 24" fill="none" stroke="#fff" stroke-width="2.4"><path d="M5 3h4l2 5-3 2a11 11 0 0 0 6 6l2-3 5 2v4a2 2 0 0 1-2 2A17 17 0 0 1 3 5a2 2 0 0 1 2-2z"/></svg>Get a Free Quote</span>
  </div>
</header>

<section class="hero" role="img" aria-label="Aerial view of a tree-lined residential neighbourhood under a navy overlay">
  <h1>A true partner, not just a vendor.</h1>
  <p>Expertise rooted in asset preservation. Discover the art of sustainable and beautiful property management.</p>
  <div class="hero-actions">
    <span class="btn">Get a Free Quote <svg viewBox="0 0 24 24" fill="none" stroke="#fff" stroke-width="2.6"><path d="M4 12h16M14 6l6 6-6 6"/></svg></span>
    <span class="btn btn-ghost"><svg viewBox="0 0 24 24" fill="none" stroke="#fff" stroke-width="2.4"><path d="M5 3h4l2 5-3 2a11 11 0 0 0 6 6l2-3 5 2v4a2 2 0 0 1-2 2A17 17 0 0 1 3 5a2 2 0 0 1 2-2z"/></svg>Call Us Now</span>
  </div>
</section>

<section class="features">
  <div class="wrap">
    <div class="feature"><h3>Competitive Rates</h3><p>Quality property management services at competitive, fair rates.</p></div>
    <div class="feature"><h3>Expert Team</h3><p>Skilled professionals dedicated to optimizing asset performance.</p></div>
    <div class="feature"><h3>Data-Driven Practices</h3><p>Advanced analytics that enhance value and protect investments.</p></div>
    <div class="feature"><h3>Client Focus</h3><p>Prioritizing owner satisfaction with personalized, attentive service.</p></div>
  </div>
</section>

<section class="about">
  <div class="about-pic" style="left:215px;top:123px;width:177px;height:220px"><div class="photo photo-green" role="img" aria-label="Aerial photo of neighbourhood homes with city skyline"></div></div>
  <div class="about-pic" style="left:403px;top:143px;width:177px;height:200px;padding-bottom:0"><div class="photo photo-green" role="img" aria-label="Aerial photo of residential streets and trees"></div></div>
  <div class="about-text">
    <div class="label">About Us</div>
    <h2 class="h2">Bringing Your Property Goals to Life</h2>
    <p>With decades of expertise in property management, we design and nurture stunning asset performance tailored to your vision. From residential properties to commercial portfolios, our team is dedicated to excellence.</p>
    <ul class="checks">
      <li><span class="tick"><svg viewBox="0 0 24 24" fill="none" stroke="#5d7f5b" stroke-width="3.5"><path d="M5 12l5 5 9-10"/></svg></span>Residential Management</li>
      <li><span class="tick"><svg viewBox="0 0 24 24" fill="none" stroke="#5d7f5b" stroke-width="3.5"><path d="M5 12l5 5 9-10"/></svg></span>Commercial Management</li>
      <li><span class="tick"><svg viewBox="0 0 24 24" fill="none" stroke="#5d7f5b" stroke-width="3.5"><path d="M5 12l5 5 9-10"/></svg></span>Multi-Family Management</li>
    </ul>
    <span class="btn">Learn More <svg viewBox="0 0 24 24" fill="none" stroke="#fff" stroke-width="2.6"><path d="M4 12h16M14 6l6 6-6 6"/></svg></span>
  </div>
</section>

<section class="services">
  <div class="wrap">
    <div class="label center">Our Services</div>
    <h2 class="h2 center">Comprehensive Property<br>Management Solutions</h2>
    <div class="svc-grid">
      <div class="svc"><div class="svc-body"><h3>Tenant Screening &amp; Placement</h3><p>Comprehensive background, credit, and reference checks ensure qualified residents.</p></div><div class="photo photo-green" role="img" aria-label="Aerial photo of residential area"></div></div>
      <div class="svc"><div class="svc-body"><h3>Lease Administration</h3><p>Full lifecycle lease management — drafting, renewals, and compliance monitoring.</p></div><div class="photo photo-green" role="img" aria-label="Aerial photo of city neighbourhood"></div></div>
      <div class="svc"><div class="svc-body"><h3>Maintenance Coordination</h3><p>Proactive maintenance programs and a vetted vendor network keep properties optimal.</p></div><div class="photo photo-wood" role="img" aria-label="Stacked timber blocks on a neutral backdrop"></div></div>
      <div class="svc"><div class="svc-body"><h3>Asset Strategy &amp; Advisory</h3><p>Strategic capital improvement planning to maximize NOI and portfolio resilience.</p></div><div class="photo photo-room" role="img" aria-label="Warm-toned interior with basin and round mirror"></div></div>
    </div>
    <div class="cta-row"><span class="btn">Explore Our Services <svg viewBox="0 0 24 24" fill="none" stroke="#fff" stroke-width="2.6"><path d="M4 12h16M14 6l6 6-6 6"/></svg></span></div>
  </div>
</section>

<section class="why">
  <div class="why-text">
    <div class="label">Why Us</div>
    <h2 class="h2">Our Commitment to Excellence</h2>
    <div class="why-item"><span class="why-icon"><svg viewBox="0 0 24 24" fill="none" stroke="#5d7f5b" stroke-width="2"><circle cx="12" cy="9" r="5"/><path d="M9 13l-2 8 5-3 5 3-2-8"/></svg></span><div><h3>Expertise &amp; Experience</h3><p>With years of industry experience, our skilled team brings unparalleled knowledge and creativity to every project.</p></div></div>
    <div class="why-item"><span class="why-icon"><svg viewBox="0 0 24 24" fill="none" stroke="#5d7f5b" stroke-width="2"><circle cx="12" cy="12" r="9"/><circle cx="12" cy="12" r="5"/><circle cx="12" cy="12" r="1.5"/></svg></span><div><h3>Customized Solutions</h3><p>We tailor our services to meet your unique needs and vision, ensuring each property reflects your investment goals.</p></div></div>
    <div class="why-item"><span class="why-icon"><svg viewBox="0 0 24 24" fill="none" stroke="#5d7f5b" stroke-width="2"><path d="M5 19C5 10 11 5 20 4c0 9-5 15-13 15M5 19l8-8"/></svg></span><div><h3>Sustainable Practices</h3><p>We prioritize proven methods and frameworks, fostering property value that respects long-term market conditions.</p></div></div>
  </div>
  <div class="why-pic photo-wood" role="img" aria-label="Stacked timber blocks topped with a stone slab"></div>
</section>

<section class="projects">
  <div class="wrap">
    <div class="label center">Our Projects</div>
    <h2 class="h2 center">Our Managed Properties</h2>
    <div class="proj-grid">
      <div class="proj photo-green" role="img" aria-label="Aerial photo of a residential portfolio with skyline"><span>Brooklyn Centre Portfolio</span></div>
      <div class="proj photo-green" role="img" aria-label="Aerial photo of mixed-use neighbourhood"><span>Akron Mixed-Use Assets</span></div>
    </div>
    <div class="cta-row"><span class="btn">View All Projects <svg viewBox="0 0 24 24" fill="none" stroke="#fff" stroke-width="2.6"><path d="M4 12h16M14 6l6 6-6 6"/></svg></span></div>
  </div>
</section>

<section class="testimonials">
  <div class="wrap">
    <div class="label center">Testimonials</div>
    <h2 class="h2 center">Honest Reviews from Our Clients</h2>
    <div class="tst-grid">
      <div class="tst">
        <div class="stars"><svg viewBox="0 0 24 24" fill="#3f5a3d"><path d="M12 2l3 7 7 .5-5.5 4.5 2 7-6.5-4-6.5 4 2-7L2 9.5 9 9z"/></svg><svg viewBox="0 0 24 24" fill="#3f5a3d"><path d="M12 2l3 7 7 .5-5.5 4.5 2 7-6.5-4-6.5 4 2-7L2 9.5 9 9z"/></svg><svg viewBox="0 0 24 24" fill="#3f5a3d"><path d="M12 2l3 7 7 .5-5.5 4.5 2 7-6.5-4-6.5 4 2-7L2 9.5 9 9z"/></svg><svg viewBox="0 0 24 24" fill="#3f5a3d"><path d="M12 2l3 7 7 .5-5.5 4.5 2 7-6.5-4-6.5 4 2-7L2 9.5 9 9z"/></svg><svg viewBox="0 0 24 24" fill="#3f5a3d"><path d="M12 2l3 7 7 .5-5.5 4.5 2 7-6.5-4-6.5 4 2-7L2 9.5 9 9z"/></svg></div>
        <blockquote>"The team at Tallgrove Vale Management totally transformed our property portfolio. Their attention to detail and expertise exceeded our expectations!"</blockquote>
        <h4>Property Owner</h4><small>Cleveland, OH</small>
      </div>
      <div class="tst">
        <div class="stars"><svg viewBox="0 0 24 24" fill="#3f5a3d"><path d="M12 2l3 7 7 .5-5.5 4.5 2 7-6.5-4-6.5 4 2-7L2 9.5 9 9z"/></svg><svg viewBox="0 0 24 24" fill="#3f5a3d"><path d="M12 2l3 7 7 .5-5.5 4.5 2 7-6.5-4-6.5 4 2-7L2 9.5 9 9z"/></svg><svg viewBox="0 0 24 24" fill="#3f5a3d"><path d="M12 2l3 7 7 .5-5.5 4.5 2 7-6.5-4-6.5 4 2-7L2 9.5 9 9z"/></svg><svg viewBox="0 0 24 24" fill="#3f5a3d"><path d="M12 2l3 7 7 .5-5.5 4.5 2 7-6.5-4-6.5 4 2-7L2 9.5 9 9z"/></svg><svg viewBox="0 0 24 24" fill="#3f5a3d"><path d="M12 2l3 7 7 .5-5.5 4.5 2 7-6.5-4-6.5 4 2-7L2 9.5 9 9z"/></svg></div>
        <blockquote>"The team at Tallgrove Vale Management totally transformed our property portfolio. Their attention to detail and expertise exceeded our expectations!"</blockquote>
        <h4>Portfolio Investor</h4><small>Akron, OH</small>
      </div>
    </div>
  </div>
</section>

<section class="cta">
  <h2>Ready to optimize your property portfolio?</h2>
  <p>Contact us today to schedule a consultation or to learn more about our services.</p>
  <span class="btn">Get A Free Quote <svg viewBox="0 0 24 24" fill="none" stroke="#3d4d73" stroke-width="2.6"><path d="M4 12h16M14 6l6 6-6 6"/></svg></span>
</section>

<section class="contact">
  <div class="wrap">
    <div class="label center">Contact Us</div>
    <h2 class="h2 center">Submit Your Property Management Inquiry</h2>
    <p class="sub center">Please complete the inquiry form to facilitate an initial consultation.</p>
    <div class="contact-grid">
      <div class="info-card">
        <h3>Get in Touch</h3>
        <div class="info-row"><span class="info-ic"><svg viewBox="0 0 24 24" fill="none" stroke="#5d7f5b" stroke-width="2"><rect x="3" y="5" width="18" height="14" rx="2"/><path d="M3 7l9 6 9-6"/></svg></span><div><small>Email</small><span>info@tallgrovevalemanagement.com</span></div></div>
        <div class="info-row"><span class="info-ic"><svg viewBox="0 0 24 24" fill="none" stroke="#5d7f5b" stroke-width="2"><path d="M12 21s-7-6-7-12a7 7 0 0 1 14 0c0 6-7 12-7 12z"/><circle cx="12" cy="9" r="2.5"/></svg></span><div><small>Service Area</small><span>Cleveland · Akron, Ohio</span></div></div>
        <div class="info-row"><span class="info-ic"><svg viewBox="0 0 24 24" fill="none" stroke="#5d7f5b" stroke-width="2"><path d="M5 3h4l2 5-3 2a11 11 0 0 0 6 6l2-3 5 2v4a2 2 0 0 1-2 2A17 17 0 0 1 3 5a2 2 0 0 1 2-2z"/></svg></span><div><small>Consultation</small><span>By appointment</span></div></div>
      </div>
      <div class="form-card">
        <div class="row2 fgroup">
          <div><label>Name</label><div class="field">Your name</div></div>
          <div><label>Email</label><div class="field">you@email.com</div></div>
        </div>
        <div class="fgroup"><label>Property Type</label><div class="field dark">Select property type</div></div>
        <div class="fgroup"><label>Message</label><div class="field tall">Tell us about your property management needs...</div></div>
        <div class="submit">Submit Inquiry <svg viewBox="0 0 24 24" fill="none" stroke="#fff" stroke-width="2.2"><path d="M22 2L11 13M22 2l-7 20-4-9-9-4z"/></svg></div>
      </div>
    </div>
  </div>
</section>

<footer class="footer">
  <div class="wrap">
    <div class="foot-grid">
      <div>
        <div class="brand"><span class="mark"></span>Tallgrove Vale</div>
        <p class="foot-about">A true partner, not just a vendor. Professional property management services for a stronger portfolio.</p>
        <div class="socials"><i></i><i></i><i></i><i></i></div>
      </div>
      <div class="foot-col"><h4>QUICK LINKS</h4><p>Home</p><p>About Us</p><p>Services</p><p>Why Us</p><p>Projects</p><p>Contact</p></div>
      <div class="foot-col"><h4>SERVICES</h4><p>Tenant Screening &amp; Placement</p><p>Lease Administration</p><p>Maintenance Coordination</p><p>Asset Strategy &amp; Advisory</p></div>
      <div class="foot-col"><h4>ADDRESS</h4>
        <p><svg viewBox="0 0 24 24" fill="none" stroke="#c3cadb" stroke-width="2"><path d="M12 21s-7-6-7-12a7 7 0 0 1 14 0c0 6-7 12-7 12z"/></svg>Cleveland · Akron, Ohio</p>
        <p><svg viewBox="0 0 24 24" fill="none" stroke="#c3cadb" stroke-width="2"><rect x="3" y="5" width="18" height="14" rx="2"/><path d="M3 7l9 6 9-6"/></svg>info@tallgrovevalemanagement.com</p>
        <p><svg viewBox="0 0 24 24" fill="none" stroke="#c3cadb" stroke-width="2"><path d="M5 3h4l2 5-3 2a11 11 0 0 0 6 6l2-3 5 2v4a2 2 0 0 1-2 2A17 17 0 0 1 3 5a2 2 0 0 1 2-2z"/></svg>By appointment</p>
      </div>
    </div>
  </div>
  <div class="copy"><span>Copyright © 2026 Tallgrove Vale Management LLC. All rights reserved.</span><span>Cleveland · Akron, Ohio</span></div>
</footer>

</body>
</html>
```